BrXpertz Business Cards for SME Experts

We need a business card for a new company based in Clearwater FL called Kestrel of Merit. KoM is your access to on-demand subject matter experts. The final design should be very clean communicating innovation and expertise. Our logo design is attached.

The Information Age has affected the workforce in that automation and computerization have resulted in higher productivity coupled with net job loss of many knowledgeable employees. Combined with the creation of the internet and search capabilities, the disintermediation of the value chain of Subject Matter Experts (SME) has happened. We no longer need to work through traditional consulting firms for all consulting needs, instead the direct access to the SME, through a leaner and lower cost model is what the market is demanding.
BrXpertz is a new marketplace to buy consulting services. The business model is that all consultants (subject matter experts) can become a consulting resource in the marketplace following our guidelines. The consumer can now easily access consultants that they could not find easily before.
In much the way an Zyla car can be identified and requested, so can a BrXpertz Consultant. Each consultant can be identified by: location, expertise, billing rate, and prior experience rating.
By seamlessly connecting consultants to requesters through a new Kestrel of Merit marketplace, you now will have an easy to use and quicker turnaround to request and staff your consulting needs. Leveraging the KoM app, you can access the subject matter expert you need for your business requirement.

Target Market(s)

Small and medium sized companies; non-profits

Industry/Entity Type

Business Consultant

Contact Information for Business Card

Name
website
email address
Logo
mailing address (debating if I really need...)
twitter
LinkedIn

Requirements
Must have
• the logo I have included in the design; want the colors to be consistent with the logo design

```html
<!DOCTYPE html>
<html lang="en">
<head>
<meta charset="utf-8">
<title>Kestrel of Merit – Business Card</title>
<link rel="stylesheet" href="https://fonts.googleapis.com/css2?family=Montserrat:wght@700&family=Open+Sans:wght@400;600&display=swap">
<style>
  :root {
    --page-bg: #e9e6e1;
    --card-navy: #25237a;
    --card-navy-deep: #1c1a63;
    --accent-cyan: #22a9c4;
    --text-white: #ffffff;
    --text-soft: #dfe2f5;
    --rule: rgba(255, 255, 255, 0.55);
    --watermark: rgba(160, 170, 230, 0.22);
  }
  html, body {
    margin: 0;
    width: 1200px;
    height: 1022px;
    overflow: hidden;
    background: var(--page-bg);
  }
  .canvas {
    position: relative;
    width: 1200px;
    height: 1022px;
  }
  .card {
    position: absolute;
    left: 150px;
    top: 254px;
    width: 900px;
    height: 514px;
    border-radius: 22px;
    overflow: hidden;
    background: linear-gradient(135deg, var(--card-navy) 0%, var(--card-navy-deep) 100%);
    box-shadow: 0 18px 40px rgba(20, 20, 60, 0.28);
    font-family: "Open Sans", Arial, sans-serif;
    color: var(--text-white);
  }
  .card__watermark {
    position: absolute;
    left: 420px;
    top: -40px;
  }
  .card__tab {
    position: absolute;
    top: -14px;
    right: 40px;
    width: 110px;
    height: 38px;
    border-radius: 14px;
    background: var(--accent-cyan);
  }
  .brand {
    position: absolute;
    left: 64px;
    top: 48px;
  }
  .brand__mark {
    width: 84px;
    height: 84px;
    border-radius: 50%;
    background: var(--accent-cyan);
  }
  .brand__name {
    margin: 34px 0 0;
    font-family: "Montserrat", Arial, sans-serif;
    font-weight: 700;
    font-size: 38px;
    letter-spacing: 0.5px;
    color: var(--text-white);
  }
  .person__name {
    position: absolute;
    left: 64px;
    top: 226px;
    margin: 0;
    font-weight: 600;
    font-size: 32px;
    letter-spacing: 1px;
  }
  .card__rule {
    position: absolute;
    left: 64px;
    right: 0;
    top: 284px;
    height: 1px;
    background: var(--rule);
  }
  .contacts {
    position: absolute;
    left: 64px;
    top: 304px;
    margin: 0;
    padding: 0;
    list-style: none;
    font-size: 24px;
    line-height: 38px;
    color: var(--text-soft);
  }
  .contacts__item {
    display: flex;
    align-items: center;
    gap: 14px;
  }
  .contacts__icon {
    width: 18px;
    height: 18px;
    flex: none;
  }
  .address {
    position: absolute;
    right: 60px;
    top: 206px;
    margin: 0;
    font-style: normal;
    font-size: 24px;
    line-height: 34px;
    text-align: left;
    color: var(--text-white);
  }
</style>
</head>
<body>
<div class="canvas">
  <article class="card" aria-label="Kestrel of Merit business card">
    <svg class="card__watermark" width="520" height="520" viewBox="0 0 520 520" aria-hidden="true">
      <circle cx="260" cy="260" r="220" fill="none" stroke="var(--watermark)" stroke-width="22"/>
    </svg>
    <div class="card__tab"></div>

    <div class="brand">
      <div class="brand__mark"></div>
      <p class="brand__name">Kestrel of Merit</p>
    </div>

    <h1 class="person__name">DANIEL REYES</h1>
    <div class="card__rule"></div>

    <ul class="contacts">
      <li class="contacts__item">
        <svg class="contacts__icon" viewBox="0 0 18 18" aria-hidden="true"><circle cx="9" cy="9" r="6" fill="var(--accent-cyan)"/></svg>
        @dan.reyes
      </li>
      <li class="contacts__item">
        <svg class="contacts__icon" viewBox="0 0 18 18" aria-hidden="true"><circle cx="9" cy="9" r="6" fill="var(--accent-cyan)"/></svg>
        dan/reyes.com
      </li>
      <li class="contacts__item">
        <svg class="contacts__icon" viewBox="0 0 18 18" aria-hidden="true">
          <rect x="1.5" y="3.5" width="15" height="11" fill="none" stroke="var(--accent-cyan)" stroke-width="1.6"/>
          <path d="M1.5 3.5 L9 10 L16.5 3.5" fill="none" stroke="var(--accent-cyan)" stroke-width="1.6"/>
        </svg>
        danreyes@postbox.com
      </li>
      <li class="contacts__item">
        <svg class="contacts__icon" viewBox="0 0 18 18" aria-hidden="true">
          <circle cx="9" cy="9" r="7.5" fill="none" stroke="var(--accent-cyan)" stroke-width="1.5"/>
          <ellipse cx="9" cy="9" rx="3.2" ry="7.5" fill="none" stroke="var(--accent-cyan)" stroke-width="1.3"/>
          <path d="M1.5 9 H16.5 M3 5 H15 M3 13 H15" stroke="var(--accent-cyan)" stroke-width="1.2"/>
        </svg>
        www.kestrelofmerit.com
      </li>
    </ul>

    <address class="address">215 W HARBOR ST<br>BROOKFIELD TX 75012</address>
  </article>
</div>
</body>
</html>
```